Buch-/E-Book-Cover für Selbsttransformation
Zielgruppe
In bin tätig als Trainer und Coach und habe meinen Schwerpunkt auf persönliche Veränderung und Transformation gelegt. Meine Zielgruppe sind Frauen (wahrscheinlich etwas überwiegend) und Männer mittleren Alters. Menschen die eine Veränderung in ihr Leben bringen wollen.
Autor: Jörg Valdemann
Aufgabenstellung
Erstellung eines Ratgeber bzw. Sachbuchcover für Paperpack und eines Ebookcoverdesign mit Druckfähigen/Ausgabefähigen Dateien für den Verlag.
Ich möchte ein modernes, eher klar und nicht zu verspieltes Design. Eventuell kann auch die Einbindung meines eigenen Bildes erfolgen. (ist aber absolut kein Muß, ihr könnt sehr eigene kreative Ideen einbringen)
In der Anlage habe ich zwei Bücher als Bild eingefügt, die mir von der Optik (Uhr als Hintergrund) und der Farbgestaltung (türkis, gelb) sehr gut gefallen. Außerdem das Bild einer Uhr, wo mir die Grafik und der Farbton sehr gut gefällt. (eventuell Schrift in Gelb oder Gold)
Der Buchtitel ist 'Mein Morgen - Mein Kompass' Wie du deine Zukunft aktiv und selbstbestimmt gestaltest. Das Buch erscheint im Torvaverlag und der Designer wird natürlich mit im Buch aufgeführt.

```html
<!DOCTYPE html>
<html lang="de">
<head>
<meta charset="utf-8">
<title>Mein Morgen - Mein Kompass – Buchcover</title>
<link rel="stylesheet" href="https://fonts.googleapis.com/css2?family=Fredoka:wght@500&family=Quicksand:wght@500&display=swap">
<style>
  :root {
    --stage: #e4e4e4;
    --orange: #c55e12;
    --teal: #417670;
    --brown: #6b5a4e;
    --cream: #e6d5bf;
    --figure-warm: #e8a23c;
    --figure-cool: #5fb1b0;
    --figure-light: #e2d3bd;
    --figure-dark: #2a2520;
  }
  * { margin: 0; padding: 0; box-sizing: border-box; }
  html, body {
    width: 1024px;
    height: 1200px;
    overflow: hidden;
    background: var(--stage);
  }
  .cover {
    position: absolute;
    left: 121px;
    top: 17px;
    width: 782px;
    height: 1165px;
    background: var(--orange);
    overflow: hidden;
  }
  .cover-shapes {
    position: absolute;
    inset: 0;
    width: 100%;
    height: 100%;
  }
  .title {
    position: absolute;
    left: 32px;
    top: 52px;
    font-family: "Fredoka", "Quicksand", sans-serif;
    font-weight: 500;
    font-size: 86px;
    line-height: 90px;
    color: var(--cream);
    letter-spacing: -1px;
    white-space: nowrap;
  }
  .subtitle {
    position: absolute;
    right: 36px;
    top: 994px;
    font-family: "Quicksand", sans-serif;
    font-weight: 500;
    font-size: 35px;
    line-height: 43px;
    color: var(--cream);
    text-align: right;
    white-space: nowrap;
  }
  .publisher {
    position: absolute;
    left: 34px;
    top: 1106px;
    width: 140px;
    text-align: center;
    font-family: "Quicksand", sans-serif;
    font-weight: 500;
    font-size: 24px;
    line-height: 30px;
    color: var(--cream);
  }
</style>
</head>
<body>
  <main class="cover">
    <svg class="cover-shapes" viewBox="0 0 1222 1821" preserveAspectRatio="none" aria-hidden="true">
      <defs>
        <linearGradient id="figureTones" x1="0" y1="0" x2="1" y2="0">
          <stop offset="0" stop-color="var(--figure-light)"/>
          <stop offset="0.4" stop-color="var(--figure-warm)"/>
          <stop offset="0.6" stop-color="var(--figure-cool)"/>
          <stop offset="1" stop-color="var(--figure-dark)"/>
        </linearGradient>
      </defs>
      <polygon class="panel-teal" points="1222,210 1222,1713 181,1713" fill="var(--teal)"/>
      <polygon class="panel-brown" points="0,980 560,1250 273,1713 248,1560 0,1683" fill="var(--brown)"/>
      <polygon class="corner-orange" points="0,1683 248,1560 273,1713 0,1713" fill="var(--orange)"/>
      <rect class="band-orange" x="0" y="1713" width="1222" height="108" fill="var(--orange)"/>
      <g role="img" aria-label="Illustration: zwei Frauen mit dunklem, lockigem Haar Rücken an Rücken, eine in warmen Orangetönen, eine in Türkistönen">
        <path class="figure-area" d="M275 1523 L275 1250 L420 1120 L440 900 L560 760 L760 745 L920 850 L980 1000 L1015 1240 L1015 1523 Z" fill="url(#figureTones)" opacity="0.9"/>
      </g>
    </svg>

    <h1 class="title">Mein Morgen -<br>Mein Kompass</h1>

    <p class="subtitle">Wie du deine Zukunft aktiv<br>und selbstbestimmt gestaltest!</p>

    <p class="publisher">Torva</p>
  </main>
</body>
</html>
```